Flyer for Luxury Boarding Stable for Retired Horses

A one page flyer to hand out at stable tours and at horse shows. Quiet Meadows at 41 Acres is a luxury equine boarding stable for retired horses. This is a new facility in Summerfield, NC that has 6 available stalls. We are trying to attract owners with 2 or more retired horses they would like to board.

Target Market(s)

Horse owners with 2 or more horses that are retired from showing, racing, or rodeo. These owners love their horses like family and want them well cared for in their retirement years.

Industry/Entity Type

Equestrian Boarding

Font styles to use
Script

Colors
EE7325
F08F49
F5BC92
FAE3D3
FDF4ED

Requirements
Must have
• Photos of the facility. Must feel upscale and worth the price.

```html
<!DOCTYPE html>
<html lang="en">
<head>
<meta charset="utf-8">
<title>Quiet Meadows at 41 Acres – Retired Horse Boarding Flyer</title>
<link rel="stylesheet" href="https://fonts.googleapis.com/css2?family=Fira+Sans:wght@400;600;700&family=Open+Sans:wght@700&family=Arimo:wght@400&family=Dancing+Script:wght@700&display=swap">
<style>
  :root {
    --canvas-bg: #efefef;
    --paper: #fdf4ed;
    --ink: #1a1411;
    --orange: #ee7325;
    --orange-soft: #f08f49;
    --peach: #f5bc92;
    --blush: #fae3d3;
    --white: #ffffff;
    --aerial-light: #b9b39f;
    --aerial-green: #4f7a36;
    --aerial-deep: #2f5426;
    --aisle-wood: #8a6a45;
    --aisle-floor: #9a9a94;
    --aisle-light: #d9d2c2;
  }
  * { box-sizing: border-box; margin: 0; padding: 0; }
  html, body { width: 1200px; height: 1200px; overflow: hidden; }
  body { background: var(--canvas-bg); position: relative; }

  .flyer {
    position: absolute;
    left: 211px;
    top: 50px;
    width: 590px;
    height: 835px;
    background: var(--paper);
    transform: scale(1.3174);
    transform-origin: top left;
    overflow: hidden;
    font-family: "Arimo", Arial, sans-serif;
    color: var(--ink);
  }

  .facility-photos { position: absolute; left: 0; top: 0; width: 590px; height: 410px; }

  .intro-quote {
    position: absolute;
    right: 32px;
    top: 298px;
    text-align: right;
    white-space: nowrap;
    font-family: "Open Sans", Verdana, sans-serif;
    font-weight: 700;
    font-size: 10.6px;
    line-height: 14.4px;
  }

  .headline {
    position: absolute;
    left: 33px;
    top: 458px;
    font-family: "Dancing Script", cursive;
    font-weight: 700;
    font-size: 24px;
    line-height: 30px;
    color: var(--orange);
  }

  .description {
    position: absolute;
    left: 33px;
    top: 506px;
    white-space: nowrap;
    font-size: 11.4px;
    line-height: 14.1px;
  }

  .call-to-action {
    position: absolute;
    left: 0;
    top: 735px;
    width: 345px;
    height: 71px;
    background: var(--peach);
    padding: 12px 0 0 33px;
    font-size: 11.2px;
    line-height: 14.4px;
  }
  .call-to-action h3 {
    font-family: "Fira Sans", Arial, sans-serif;
    font-weight: 600;
    font-size: 13.5px;
    line-height: 15px;
  }

  .values-panel {
    position: absolute;
    left: 345px;
    top: 423px;
    width: 245px;
    height: 383px;
    background: var(--orange);
    border-top-left-radius: 52px;
  }
  .values-list {
    position: absolute;
    right: 32px;
    top: 17px;
    text-align: right;
    white-space: nowrap;
    color: var(--white);
    font-family: "Dancing Script", cursive;
    font-weight: 700;
    font-size: 21px;
    line-height: 21px;
  }

  .fees-panel {
    position: absolute;
    left: 370px;
    top: 550px;
    width: 220px;
    height: 256px;
    background: var(--peach);
    border-top-left-radius: 44px;
    box-shadow: -2px 3px 6px rgba(0,0,0,0.3);
    text-align: right;
    padding: 25px 32px 0 0;
    font-family: "Fira Sans", Arial, sans-serif;
  }
  .fees-title { font-weight: 700; font-size: 16.5px; line-height: 20px; margin-bottom: 13px; }
  .fee { height: 64px; }
  .fee-tier { font-weight: 700; font-size: 16px; line-height: 20px; }
  .fee-price { font-weight: 400; font-size: 16px; line-height: 20px; }
</style>
</head>
<body>
  <main class="flyer">
    <svg class="facility-photos" viewBox="0 0 590 410" width="590" height="410">
      <defs>
        <linearGradient id="aerial-grove" x1="0" y1="0" x2="1" y2="1">
          <stop offset="0" stop-color="#2f5426"/>
          <stop offset="1" stop-color="#4f7a36"/>
        </linearGradient>
        <radialGradient id="aerial-barn" cx="0.5" cy="0.55" r="0.6">
          <stop offset="0" stop-color="#b9b39f"/>
          <stop offset="0.6" stop-color="#9fa88a"/>
          <stop offset="1" stop-color="#4f7a36"/>
        </radialGradient>
        <linearGradient id="barn-aisle" x1="0" y1="0" x2="0" y2="1">
          <stop offset="0" stop-color="#8a6a45"/>
          <stop offset="0.45" stop-color="#d9d2c2"/>
          <stop offset="1" stop-color="#9a9a94"/>
        </linearGradient>
      </defs>
      <polygon role="img" aria-label="Aerial view of tree-lined drive and guest house" points="0,0 75,0 140,65 0,205" fill="url(#aerial-grove)"/>
      <polygon role="img" aria-label="Aerial view of treetops and parking area" points="95,0 205,0 150,55" fill="url(#aerial-grove)"/>
      <polygon role="img" aria-label="Aerial view of the main barn surrounded by lawns and evergreens" points="210,18 402,210 210,402 18,210" fill="url(#aerial-barn)"/>
      <polygon role="img" aria-label="Interior barn aisle lined with wooden horse stalls" points="225,0 590,0 590,23 418,195" fill="url(#barn-aisle)"/>
    </svg>

    <p class="intro-quote">Horse owners who love their horses like<br>family. They wouldn't put their parents<br>into an inferior retirement home receiving<br>sub par care - they demand quality facilities<br>and treatment. They have the same requirements<br>for their retired horses.</p>

    <h1 class="headline">Quiet Meadows at 41 Acres</h1>

    <p class="description">Now available a premier retirement horse boarding<br>facility, where luxury meets equestrian<br>excellence! We have 6 available stalls, conveniently<br>located in Summerfield, NC. Our facility offers top tier<br>amenities where every detail is meticulously crafted<br>to ensure quality care for your retired equine<br>companions. From spacious stalls with back patios to<br>lush pastures for gentle exercise, every detail is<br>crafted to ensure well being. You have access to a<br>world class riding arena with stadium lights, miles of<br>trails through 41 acres, top quality feed and hay, and<br>passionate, loving care from a staff with decades of<br>experience.</p>

    <section class="call-to-action">
      <h3>Call to Action:</h3>
      <p>Contact us for a tour of Quiet Meadows at 41 Acres.<br>Call or text Marianne at 336-555-0148</p>
    </section>

    <section class="values-panel">
      <p class="values-list">Luxurious.<br>Quality Facilities.<br>Loving Care.<br>Peaceful. Kind.</p>
    </section>

    <section class="fees-panel">
      <h2 class="fees-title">BOARDING FEES:</h2>
      <div class="fee"><div class="fee-tier">1st horse</div><div class="fee-price">$1,100/mo</div></div>
      <div class="fee"><div class="fee-tier">2nd horse</div><div class="fee-price">$900/mo</div></div>
      <div class="fee"><div class="fee-tier">3rd horse</div><div class="fee-price">$700/mo</div></div>
    </section>
  </main>
</body>
</html>
```